Business Card Ayurvedic Massage

I'm starting with my ayurvedic massage business and need a business card design. The design should be inline with my brand/logo as well as with the design of my website (www.lumo-thara.ch).
Front: logo and text "Ayurvedische Massagen"
back: name and adress (see details https://www.lumo-thara.ch/kontakt.html)

```html
<!DOCTYPE html>
<html lang="de">
<head>
<meta charset="utf-8">
<title>lumo-thara – Visitenkarte</title>
<link rel="stylesheet" href="https://fonts.googleapis.com/css2?family=Lato:wght@400;700&family=Tinos&display=swap">
<style>
  :root {
    --stage: #1c1c1c;
    --red-light: #8c1619;
    --red-dark: #6a0f12;
    --card-black: #141414;
    --gold: #e3b43d;
    --gold-soft: #ecd3a0;
    --elephant-gold: #d9a232;
    --elephant-red: #a8221e;
  }
  * { margin: 0; padding: 0; box-sizing: border-box; }
  html, body { width: 1200px; height: 1200px; overflow: hidden; background: var(--stage); }
  .canvas { position: relative; width: 1200px; height: 1200px; }

  .card { position: absolute; box-shadow: 0 10px 24px rgba(0,0,0,.6); }

  .card-front {
    left: 187px; top: 86px; width: 823px; height: 474px;
    background: linear-gradient(180deg, var(--red-light) 0%, #7e1316 60%, var(--red-dark) 100%);
  }
  .front-backdrop {
    position: absolute; inset: 0;
    background: radial-gradient(ellipse at 50% 45%, rgba(110,14,18,.55) 0%, rgba(110,14,18,0) 70%);
  }
  .elephant {
    position: absolute; top: 146px; width: 146px; height: 184px;
    border-radius: 40% 40% 14% 14%;
    background: linear-gradient(160deg, var(--elephant-gold) 0%, var(--elephant-red) 55%, var(--elephant-gold) 100%);
    opacity: .85;
  }
  .elephant-left { left: 137px; }
  .elephant-right { left: 537px; }
  .brand-name {
    position: absolute; left: 0; right: 0; top: 232px;
    text-align: center;
    font-family: "Lato", sans-serif; font-weight: 700;
    font-size: 40px; color: var(--gold); letter-spacing: 1px;
  }
  .tagline {
    position: absolute; left: 0; right: 0; top: 336px;
    text-align: center;
    font-family: "Tinos", serif; font-size: 25px;
    color: var(--gold-soft); letter-spacing: .5px;
  }

  .card-back {
    left: 187px; top: 640px; width: 835px; height: 466px;
    background: var(--card-black);
    font-family: "Lato", sans-serif; color: var(--gold);
    text-align: center;
  }
  .notice { position: absolute; left: 0; right: 0; top: 116px; font-size: 42px; }
  .address { position: absolute; left: 0; right: 0; top: 190px; font-size: 24px; line-height: 34px; }
  .contact { position: absolute; left: 0; right: 0; top: 274px; font-size: 24px; line-height: 33px; }
</style>
</head>
<body>
<div class="canvas">
  <section class="card card-front">
    <div class="front-backdrop" role="img" aria-label="Faded red photograph of an Indian palace with damask pattern"></div>
    <div class="elephant elephant-left" role="img" aria-label="Ornate golden decorated elephant with parasol"></div>
    <div class="brand-name">lumo-thara</div>
    <div class="elephant elephant-right" role="img" aria-label="Ornate golden decorated elephant with parasol, mirrored"></div>
    <p class="tagline">AYURVEDISCHE MASSAGEN</p>
  </section>

  <section class="card card-back">
    <h1 class="notice" style="font-weight:400">Bitte keine Werbung</h1>
    <p class="address">Mira Tanner, lumo-thara<br>Lindenweg 14, 8853 Lachen (SZ)</p>
    <p class="contact">+41 77 555 01 23<br>info@lumo-thara.ch<br>www.lumo-thara.ch</p>
  </section>
</div>
</body>
</html>
```